Popular Miami Restaurant & Bar looking for a new ad!!!

We are a high volume restaurant & bar that is constantly running great food and drink specials to keep people coming over and over again. We run ads every week and have been creating them through an ad agency and there ads have gotten to be very boring and bland to me. You can visit our website at www.pellicanos.com to see what our menu is like, get our logo and our colors. I will also attach our last ad (which I think looks too busy and boring). I will also attach food pics and our logo. We have an american menu with a good bar crowd, a lot of steaks, chicken, fish and salads. Our clientele is typically a little older and we are starting to do entertainment from Wednesday through Saturday nights. We are going to run a different special everyday of the week as well and want this ad to portray our new specials and entertainment. It will be placed full page in the Coral Ledger, Gulfshore Daily Courier, Palmetto Gazette and Bayside Reef Pages. We are spending approx. $5,000 a week in advertising and will continue to do so with this new ad.
I would like to see some designs that have a calendar feel to them with the following specials.
Wednesdays: 18 oz Bone In New York Strip with a side for $15.95
with classic oldies and light rock performed by Rusty & Marco
Thursdays: Filet Mignon Kebob with a side for $15.95 and Benny and Tremolos performing Doo Wop all night long.
Fridays: 20 oz T Bone Steak with a side for $15.95 Harlan Whitcombe Quartet performing Light jazz
Saturdays: 18 oz bone in rib eye with a side for $15.95 with Odalys performing Latin and american hits
Sunday through Tuesday is our 2 for $22 special. Two people come and share an appetizer choose your entree with sides and a dessert to share for only $22!!!
Please email me any questions.
Updates
First placement is a gatefold ad in a newspaper. Dimensions are 4.50" wide x 20" high
The top half of this ad will be the cover of the newspaper so that is the most important piece to use and grab attention.
Industry/Entity Type
Entertainment
Requirements
Must have
- Logo, add Grill and Bar under it.
Address
Phone #
Website
Nice to have
- Attached food shots. These are actual shots of our food taken durning a photo shoot. I think it would be nice that people see these shots of our specials were running.
Some sort of image for the 2 for $22 special.

```html
<!DOCTYPE html>
<html lang="en">
<head>
<meta charset="utf-8">
<title>Pellicano's Grill &amp; Bar – Weekly Specials</title>
<link rel="stylesheet" href="https://fonts.googleapis.com/css2?family=Yanone+Kaffeesatz:wght@500;700&family=Oswald:wght@500;700&family=Roboto+Condensed:wght@400;700&display=swap">
<style>
  :root {
    --brown: #4a2410;
    --brown-deep: #3a1b0b;
    --yellow: #fde98c;
    --yellow-soft: #fbe07a;
    --gold: #f2cf67;
    --wine: #8c2232;
    --cream: #fff8e6;
    --white: #ffffff;
  }
  * { box-sizing: border-box; margin: 0; padding: 0; }
  html, body { width: 1200px; height: 5337px; overflow: hidden; background: var(--brown); }
  .ad { position: relative; width: 1200px; height: 5337px; overflow: hidden; background: var(--brown); font-family: "Roboto Condensed", sans-serif; }

  .hero-photo { position: absolute; left: 0; top: 0; width: 1200px; height: 800px;
    background: radial-gradient(ellipse 48% 40% at 40% 52%, #f4f1ea 0%, #d9d3c7 55%, #6b3a1e 80%, var(--brown) 100%); }
  .site-url { position: absolute; top: 78px; left: 0; width: 1200px; text-align: center; color: var(--gold);
    font-size: 48px; font-weight: 700; letter-spacing: 1px; }

  .brand { position: absolute; top: 800px; left: 0; width: 1200px; text-align: center; color: var(--white); }
  .brand-name { font-family: "Roboto Condensed", sans-serif; font-weight: 400; font-size: 170px; line-height: 1; }
  .brand-sub { font-size: 58px; letter-spacing: 14px; margin-top: 6px; }

  .steak-photo { position: absolute; left: 650px; top: 1110px; width: 620px; height: 520px; border-radius: 50%;
    background: radial-gradient(ellipse at 45% 45%, #7a3d1c 0%, #5a2a12 45%, #e9e4da 70%, #d8d2c5 100%); }

  .headline { position: absolute; left: 82px; top: 1120px; font-family: "Yanone Kaffeesatz", sans-serif;
    font-weight: 700; font-size: 165px; line-height: 215px; color: var(--white); }
  .headline .accent { color: var(--gold); }

  .day { position: absolute; left: 0; width: 1200px; overflow: hidden; }
  .day--light { background: linear-gradient(90deg, var(--yellow) 0%, var(--yellow-soft) 100%); }
  .day--dark { background: linear-gradient(90deg, var(--yellow) 0, var(--yellow) 407px, var(--brown) 407px, var(--brown-deep) 100%); }
  .day .photo-tab { position: absolute; left: 44px; top: 52px; }
  .day-title { position: absolute; left: 452px; top: 50px; font-family: "Oswald", sans-serif; font-weight: 700;
    font-size: 64px; line-height: 1; text-transform: uppercase; }
  .day-title--mixed { text-transform: none; }
  .day-dish { position: absolute; left: 452px; top: 132px; font-size: 30px; }
  .day-price { position: absolute; left: 446px; top: 180px; font-family: "Yanone Kaffeesatz", sans-serif; font-weight: 700;
    font-size: 210px; line-height: 1; white-space: nowrap; }
  .day-price sup { font-size: 120px; vertical-align: 62px; }
  .day-act { position: absolute; left: 452px; top: 420px; font-size: 30px; line-height: 40px; }
  .act-photo { position: absolute; left: 870px; top: 120px; width: 350px; height: 350px; border-radius: 50%;
    border: 8px solid var(--brown-deep); }

  .day--light .day-title { color: var(--brown); }
  .day--light .day-dish { color: var(--brown); }
  .day--light .day-price { color: var(--wine); }
  .day--light .day-act { color: var(--wine); font-weight: 700; }
  .day--dark .day-title { color: var(--gold); }
  .day--dark .day-dish { color: var(--cream); }
  .day--dark .day-price { color: var(--white); }
  .day--dark .day-act { color: var(--cream); font-weight: 700; }

  .combo-copy { position: absolute; left: 452px; top: 132px; font-size: 31px; line-height: 44px; color: var(--brown); font-weight: 700; }
  .combo-price { position: absolute; right: 120px; top: 270px; text-align: right; font-family: "Yanone Kaffeesatz", sans-serif;
    font-weight: 700; color: var(--wine); line-height: 1; white-space: nowrap; }
  .combo-price .big { font-size: 200px; margin-right: 80px; }
  .combo-price .tag { font-size: 120px; margin-top: -20px; }

  .footer { position: absolute; left: 0; top: 4937px; width: 1200px; height: 400px; background: var(--brown-deep);
    text-align: center; color: var(--white); }
  .footer-line { font-size: 40px; line-height: 64px; }
  .footer-info { padding-top: 42px; }
  .footer-line .accent { color: var(--gold); }
  .footer-note { margin-top: 44px; font-size: 24px; line-height: 36px; }
</style>
</head>
<body>
<div class="ad">
  <div class="hero-photo" role="img" aria-label="Photo of a grilled steak with broccoli and carrots on a white plate"></div>
  <div class="site-url">www.pellicanos.com</div>

  <div class="brand">
    <div class="brand-name">Pellicano's</div>
    <div class="brand-sub">GRILL &amp; BAR</div>
  </div>

  <div class="steak-photo" role="img" aria-label="Photo of a T-bone steak with green beans on a plate"></div>
  <h1 class="headline">Every Day Is<br>Special At<br><span class="accent">South Florida's</span><br><span class="accent">Favorite Grill &amp; Bar!</span></h1>

  <section class="day day--light" style="top:1989px;height:578px">
    <svg class="photo-tab" width="372" height="411" viewBox="0 0 372 411"><path d="M0 0H326L372 40L326 80V411H0Z" fill="var(--brown)"/></svg>
    <h2 class="day-title">Wednesdays</h2>
    <p class="day-dish">18oz Bone In New York Strip with a side</p>
    <p class="day-price"><sup>$</sup>15.95</p>
    <p class="day-act">with classic oldies and light rock<br>performed by Rusty &amp; Marco</p>
    <div class="act-photo" role="img" aria-label="Promotional photo of the performing duo" style="background:radial-gradient(circle,#f3c98a,#4fa6b8)"></div>
  </section>

  <section class="day day--dark" style="top:2567px;height:581px">
    <svg class="photo-tab" width="372" height="411" viewBox="0 0 372 411"><path d="M0 0H326L372 40L326 80V411H0Z" fill="var(--brown)"/></svg>
    <h2 class="day-title">Thursdays</h2>
    <p class="day-dish">Filet Mignon Kebob with a side</p>
    <p class="day-price"><sup>$</sup>15.95</p>
    <p class="day-act">Benny and Tremolos<br>performing Doo Wop all night long</p>
    <div class="act-photo" role="img" aria-label="Promotional photo of the doo wop group" style="background:radial-gradient(circle,#5a6a78,#1b1b1f)"></div>
  </section>

  <section class="day day--light" style="top:3148px;height:578px">
    <svg class="photo-tab" width="372" height="411" viewBox="0 0 372 411"><path d="M0 0H326L372 40L326 80V411H0Z" fill="var(--brown)"/></svg>
    <h2 class="day-title day-title--mixed">fridays</h2>
    <p class="day-dish">20 oz T Bone Steak with a side</p>
    <p class="day-price"><sup>$</sup>15.95</p>
    <p class="day-act">Harlan Whitcombe Quartet<br>performing Light jazz</p>
    <div class="act-photo" role="img" aria-label="Promotional photo of the jazz quartet" style="background:radial-gradient(circle,#d9a27a,#3a2216)"></div>
  </section>

  <section class="day day--dark" style="top:3726px;height:578px">
    <svg class="photo-tab" width="372" height="411" viewBox="0 0 372 411"><path d="M0 0H326L372 40L326 80V411H0Z" fill="var(--brown)"/></svg>
    <h2 class="day-title day-title--mixed">Saturdays</h2>
    <p class="day-dish">18 oz bone in rib eye with a side</p>
    <p class="day-price"><sup>$</sup>15.95</p>
    <p class="day-act">Odalys<br>performing Latin and american hits</p>
    <div class="act-photo" role="img" aria-label="Promotional photo of the singer" style="background:radial-gradient(circle,#f3c98a,#4fa6b8)"></div>
  </section>

  <section class="day day--light" style="top:4304px;height:633px">
    <svg class="photo-tab" width="372" height="411" viewBox="0 0 372 411"><path d="M0 0H326L372 40L326 80V411H0Z" fill="var(--brown)"/></svg>
    <h2 class="day-title day-title--mixed">Sunday – Tuesday</h2>
    <p class="combo-copy">Two people come and share<br>an appetizer choose your entree<br>with sides and a dessert to share</p>
    <div class="combo-price">
      <div class="big">2 for $22</div>
      <div class="tag">SPECIAL</div>
    </div>
  </section>

  <footer class="footer">
    <div class="footer-info">
      <p class="footer-line">240 Harbor Palm Avenue, Seabreeze Cove</p>
      <p class="footer-line">954.555.0182 &nbsp;|&nbsp; See our menu online at www.pellicanos.com</p>
      <p class="footer-line">11:30am - 1am, 7 days a week &nbsp;|&nbsp; <span class="accent">Reservations accepted</span></p>
    </div>
    <p class="footer-note">All Specials listed above include choice of French fries,<br>baked potato, or steamed vegetables. No Sharing</p>
  </footer>
</div>
</body>
</html>
```